Infographic for CPA Firm Lead Magnet

I need a one page infographic for a lead magnet for my CPA firm. The name of the lead magnet will be "Hidden Perks Nobody Mentions About Ledger Pros". The lead magnet will need to have my firm logo (attached) on it, or watermarked on it. The attached Excel file has the three content categories which are the content basis for the infographic. My website is cedarlinecpa.com to give you a better sense of my branding. Feel free to use whichever logo version you think is appropriate, and to take whatever information you deem appropriate from my website.

Target Market(s)

Business owners/entrepreneurs

Industry/Entity Type

Accounting

Font styles to use
Sans Serif

Colors

Designer to choose colors to be used in the design.

Requirements
Must have
• Must have each category and item listed on the Excel file. Must also have my logo or my logo watermarked.

```html
<!DOCTYPE html>
<html lang="en">
<head>
<meta charset="utf-8">
<title>Hidden Perks Nobody Mentions About Ledger Pros</title>
<link href="https://fonts.googleapis.com/css2?family=Source+Sans+3:wght@400;600;700;800&display=swap" rel="stylesheet">
<style>
:root{
  --bg:#a3a3a5;
  --navy:#3b3f5e;
  --pink:#d6506c;
  --mint:#b9eed6;
  --teal:#4f9e95;
  --green:#2f7d52;
  --title:#2d6a3e;
  --white:#ffffff;
}
*{box-sizing:border-box;margin:0;padding:0}
html,body{width:1200px;height:1200px;overflow:hidden}
body{background:var(--bg);font-family:"Source Sans 3",Arial,sans-serif;position:relative}
.abs{position:absolute}
.headline{left:0;width:1200px;top:14px;text-align:center;color:var(--title);font-size:40px;font-weight:700}
.brand{left:120px;top:100px;width:152px;text-align:center;color:var(--navy);font-weight:800;font-size:30px;line-height:1;letter-spacing:1px}
.brand small{display:block;font-size:12px;letter-spacing:2px;margin-top:6px;font-weight:800}
.spine{left:614px;top:92px;width:9px;height:1052px;background:var(--white)}
.spine-cap{left:598px;width:41px;height:6px;background:var(--white)}
.tag{position:absolute;height:50px;display:flex;align-items:center;justify-content:center;text-align:center;color:var(--white);font-weight:700;font-size:18px;line-height:1.05;padding:0 12px 0 24px}
.tag.tag-small{font-size:15px}
.tag-left{left:391px;width:205px;clip-path:polygon(16px 0,100% 0,100% 100%,16px 100%,0 50%)}
.tag-right{left:631px;width:205px;clip-path:polygon(0 0,100% 0,100% 100%,0 100%,16px 50%)}
.tag.navy{background:var(--navy)}.tag.pink{background:var(--pink)}.tag.teal{background:var(--teal)}
.tag.mint{background:var(--mint);color:var(--navy)}
/* wayfinder column */
.step-label{left:161px;width:116px;display:flex;align-items:center;justify-content:center;text-align:center;font-weight:800;font-size:15px;line-height:1.05;color:var(--white)}
.hex{left:115px;width:209px;clip-path:polygon(50% 0,100% 18%,100% 82%,50% 100%,0 82%,0 18%);display:flex;align-items:center;justify-content:center;text-align:center;padding:30px 24px 16px;font-size:14px;font-weight:600;line-height:1.25}
.hex-num{left:160px;width:118px;height:56px;clip-path:polygon(25% 0,75% 0,100% 50%,75% 100%,25% 100%,0 50%);display:flex;align-items:center;justify-content:center}
.hex-num span{width:42px;height:42px;border-radius:50%;border:2px solid rgba(255,255,255,.6);color:var(--white);font-weight:700;font-size:26px;display:flex;align-items:center;justify-content:center;background:rgba(255,255,255,.15)}
/* right column */
.group-title{left:888px;color:#c8304f;font-weight:700;font-size:21px}
.known{left:900px;width:210px;height:72px;border-radius:36px;display:flex;align-items:center;color:var(--white);font-weight:700;font-size:19px;line-height:1.1}
.known .num{width:54px;height:54px;border-radius:50%;background:var(--white);margin:0 18px 0 10px;flex:none;display:flex;align-items:center;justify-content:center;font-size:32px;font-weight:400}
.known-tail{width:0;height:0;border-style:solid}
.maybe{left:912px;width:192px;height:74px;border-radius:0 37px 37px 0;display:flex;align-items:center;justify-content:center;text-align:center;color:var(--white);font-weight:800;font-size:18px;line-height:1.05;padding:16px 18px 0 18px}
.maybe.white{background:var(--white);color:#111}
.pin{left:922px;width:50px;height:50px;border-radius:50%;background:var(--navy);border:5px solid var(--bg);outline:2px solid var(--white);outline-offset:-9px;color:var(--white);font-weight:700;font-size:15px;display:flex;align-items:center;justify-content:center}
</style>
</head>
<body>
<h1 class="abs headline">But Did You Know?</h1>

<div class="abs brand">CEDARLINE<small>CPA</small></div>

<div class="abs spine"></div>
<div class="abs spine-cap" style="top:92px"></div>
<div class="abs spine-cap" style="top:1138px"></div>

<div class="tag tag-left navy" style="top:117px">Benchmarking</div>
<div class="tag tag-left mint" style="top:215px">Budgeting</div>
<div class="tag tag-left pink tag-small" style="top:311px">Business Acquisition Due Diligence</div>
<div class="tag tag-left teal tag-small" style="top:407px">Business Management Reports</div>
<div class="tag tag-left navy" style="top:508px">Business Plans</div>
<div class="tag tag-left mint" style="top:608px">Business Strategy Consulting</div>
<div class="tag tag-left pink" style="top:705px">Business Valuation</div>
<div class="tag tag-left teal" style="top:803px">Cash Flow Management</div>
<div class="tag tag-left navy tag-small" style="top:902px">Choice of Legal Structure Consulting</div>
<div class="tag tag-left mint" style="top:983px">Dashboards</div>
<div class="tag tag-left pink" style="top:1074px">Divorce Consulting</div>

<div class="tag tag-right pink" style="top:151px">Financial Forecasting</div>
<div class="tag tag-right navy" style="top:252px">Internal Controls Consulting</div>
<div class="tag tag-right navy tag-small" style="top:352px">Key Performance Indicator Development</div>
<div class="tag tag-right pink" style="top:460px">Local Taxes</div>
<div class="tag tag-right teal" style="top:558px">Payroll Tax Returns</div>
<div class="tag tag-right navy" style="top:659px">Performance Tracking</div>
<div class="tag tag-right mint tag-small" style="top:755px">Profitability Analysis</div>
<div class="tag tag-right pink" style="top:854px">Sales Tax Returns</div>
<div class="tag tag-right teal tag-small" style="top:950px">Software Consulting &amp; Implementation</div>
<div class="tag tag-right navy tag-small" style="top:1032px">Succession Planning</div>

<!-- wayfinder column -->
<div class="abs step-label" style="top:314px;height:38px;background:var(--white);color:#111">WAYFINDER</div>
<div class="abs hex" style="top:398px;height:136px;background:var(--white);color:#222">Maybe you're not sure how to measure your business's performance.</div>
<div class="abs hex-num" style="top:352px;background:var(--navy)"><span>1</span></div>

<div class="abs step-label" style="top:530px;height:44px;background:var(--pink)">OUTSOURCED<br>ACCOUNTING</div>
<div class="abs hex" style="top:612px;height:150px;background:var(--mint);color:#222">The balance sheet in this stock photo doesn't actually balance. The photo is still cool, so I'm going to</div>
<div class="abs hex-num" style="top:574px;background:var(--pink)"><span>2</span></div>

<div class="abs step-label" style="top:766px;height:44px;background:var(--navy)">TAX<br>PREPARATION</div>
<div class="abs hex" style="top:848px;height:210px;background:var(--pink);color:var(--white)">Expenses of whaling captains are deductible as charitable contributions in the tax code. It's</div>
<div class="abs hex-num" style="top:810px;background:var(--navy)"><span>3</span></div>

<!-- already know -->
<div class="abs group-title" style="top:94px">THINGS YOU ALREADY KNOW…</div>
<div class="abs known" style="top:150px;background:var(--navy)"><span class="num" style="color:var(--pink)">1</span>Accounting &amp;<br>Bookkeeping</div>
<div class="abs known-tail" style="left:932px;top:218px;border-width:14px 10px 0 10px;border-color:var(--navy) transparent transparent transparent"></div>
<div class="abs known" style="top:268px;background:var(--pink)"><span class="num" style="color:var(--pink)">2</span>Federal Taxes</div>
<div class="abs known-tail" style="left:932px;top:336px;border-width:14px 10px 0 10px;border-color:var(--pink) transparent transparent transparent"></div>
<div class="abs known" style="top:384px;background:var(--green)"><span class="num" style="color:#111">3</span>State Taxes</div>
<div class="abs known-tail" style="left:932px;top:452px;border-width:14px 10px 0 10px;border-color:var(--green) transparent transparent transparent"></div>

<!-- may know -->
<div class="abs group-title" style="top:520px">THINGS YOU MAY KNOW…</div>
<div class="abs maybe white" style="top:610px">1099 ISSUANCE</div>
<div class="abs maybe" style="top:718px;background:var(--navy)">FINANCIAL<br>PLANNING</div>
<div class="abs maybe" style="top:830px;background:var(--pink)">IRS RESOLUTION</div>
<div class="abs maybe" style="top:934px;background:var(--green)">PAYROLL</div>
<div class="abs maybe" style="top:1036px;height:86px;background:var(--navy)">TAX<br>PLANNING</div>
<div class="abs pin" style="top:556px">01</div>
<div class="abs pin" style="top:680px">02</div>
<div class="abs pin" style="top:788px">03</div>
<div class="abs pin" style="top:894px">04</div>
<div class="abs pin" style="top:990px">05</div>
</body>
</html>
```